NEW Modern Sleek Business Card for VR Language Startup

Our startup is using VR to lead the next wave of world language education. We need a two-sided business card that introduces the larger organization (Quorvel Language Inc) and our contact info on one side and shows the product, Lumidrasca, on the other side.

Side 1 (contact info)= Quorvel Logo and Contact info (name, title, phone, email)

Side 2 (product)= Lumidrasc logo, text, and website
Text= Culturally Immersive Language Learning Games
Website= www.lumidrasc.example

Target Market(s)

Education, Technology

Contact Information for Business Card

Contact info will be updated upon approval of the design. For now, put this as a placeholder.

Perry Hollins
Founder & CEO
phollins@mailtrove.example
(555)-014-2736

Font styles to use
Other font styles liked:
• Gibson and Century Gothic are the brand fonts

Requirements
Nice to have
• I would love to see cohesion between the design and colors of the two logos. I have attached a few business card designs that I like, so you can get a feel for my preferred style.

```html
<!DOCTYPE html>
<html lang="en">
<head>
<meta charset="utf-8">
<title>Quorvel Language – Business Card</title>
<link rel="stylesheet" href="https://fonts.googleapis.com/css2?family=Montserrat:wght@600;800&family=Questrial&display=swap">
<style>
  :root {
    --backdrop: #3a3a3c;
    --white: #ffffff;
    --ink: #4d4d4f;
    --ink-soft: #5a5a5c;
    --sun: #f7b23b;
    --coral: #ee2f46;
    --plum: #a4318f;
    --violet: #7762aa;
    --sky: #4fc9d9;
    --azure: #3a9fe0;
  }
  * { margin: 0; padding: 0; box-sizing: border-box; }
  html, body { width: 984px; height: 1200px; overflow: hidden; }
  body { background: var(--backdrop); position: relative; font-family: "Questrial", "Century Gothic", sans-serif; }

  .card {
    position: absolute;
    left: 171px;
    width: 642px;
    height: 416px;
    border-radius: 32px;
    overflow: hidden;
  }
  .card--front {
    top: 158px;
    background: linear-gradient(152deg, var(--sun) 0%, var(--coral) 30%, var(--plum) 52%, var(--violet) 72%, var(--sky) 100%);
    color: var(--white);
  }
  .card--back { top: 626px; background: var(--white); color: var(--ink); }

  .identity {
    position: absolute; top: 34px; left: 0; right: 0;
    display: flex; justify-content: center; align-items: baseline; gap: 26px;
  }
  .identity__name { font-family: "Montserrat", sans-serif; font-weight: 800; font-size: 17px; letter-spacing: 8px; }
  .identity__title { font-size: 12px; letter-spacing: 5px; }

  .brand { position: absolute; display: flex; align-items: center; }
  .brand--company { top: 160px; left: 150px; gap: 26px; }
  .brand__mark { width: 92px; height: 92px; border-radius: 50%; background: var(--white); flex: none; }
  .brand__words { font-family: "Montserrat", sans-serif; font-weight: 600; color: var(--white); line-height: 1; }
  .brand__main { display: block; font-size: 50px; letter-spacing: 3px; }
  .brand__sub { display: block; font-size: 21px; letter-spacing: 12px; margin-top: 12px; padding-left: 14px; }

  .contacts {
    position: absolute; top: 365px; left: 41px; right: 24px;
    display: flex; align-items: center; gap: 30px;
  }
  .contact { display: flex; align-items: center; gap: 12px; white-space: nowrap; }
  .contact__icon { width: 24px; height: 24px; flex: none; }
  .contact__text--email { font-size: 14px; letter-spacing: 2.3px; }
  .contact__text--phone { font-size: 15px; letter-spacing: 5px; }

  .brand--product { top: 84px; left: 0; right: 0; flex-direction: column; gap: 12px; }
  .brand__mark--product { width: 110px; height: 110px; background: var(--azure); }
  .brand__product-name { font-family: "Questrial", sans-serif; font-size: 42px; color: var(--ink); line-height: 1; }

  .tagline {
    position: absolute; top: 264px; left: 0; right: 0; text-align: center;
    font-size: 15px; letter-spacing: 6.5px; line-height: 24px; color: var(--ink-soft);
  }
  .website {
    position: absolute; top: 374px; left: 0; right: 0;
    display: flex; justify-content: center; align-items: center; gap: 16px;
    font-size: 15px; letter-spacing: 7px; color: var(--ink);
  }
  .website__icon { width: 25px; height: 25px; }
</style>
</head>
<body>

<section class="card card--front">
  <div class="identity">
    <span class="identity__name">PERRY HOLLINS</span>
    <span class="identity__title">FOUNDER &amp; CEO</span>
  </div>

  <div class="brand brand--company">
    <span class="brand__mark"></span>
    <span class="brand__words">
      <span class="brand__main">QUORVEL</span>
      <span class="brand__sub">LANGUAGE</span>
    </span>
  </div>

  <div class="contacts">
    <div class="contact">
      <svg class="contact__icon" viewBox="0 0 24 24" aria-hidden="true">
        <circle cx="12" cy="12" r="12" fill="#fff"/>
        <rect x="5.5" y="7.5" width="13" height="9" rx="1" fill="none" stroke="#c23a78" stroke-width="1.4"/>
        <path d="M5.8 8l6.2 5 6.2-5M5.8 16l4.6-4.2M18.2 16l-4.6-4.2" fill="none" stroke="#c23a78" stroke-width="1.2"/>
      </svg>
      <span class="contact__text contact__text--email">phollins@mailtrove.example</span>
    </div>
    <div class="contact">
      <svg class="contact__icon" viewBox="0 0 24 24" aria-hidden="true">
        <circle cx="12" cy="12" r="12" fill="#fff"/>
        <path d="M8.2 5.8l2 3.2-1.3 1.4c.8 1.8 2.3 3.4 4.1 4.3l1.4-1.3 3.2 2-1 2.4c-4.8.2-9.5-4.5-9.4-9.6z" fill="none" stroke="#8a5ca6" stroke-width="1.4" stroke-linejoin="round"/>
      </svg>
      <span class="contact__text contact__text--phone">(555)-014-2736</span>
    </div>
  </div>
</section>

<section class="card card--back">
  <div class="brand brand--product">
    <span class="brand__mark brand__mark--product"></span>
    <span class="brand__product-name">Lumidrasc</span>
  </div>

  <p class="tagline">CULTURALLY IMMERSIVE<br>LANGUAGE LEARNING GAMES</p>

  <div class="website">
    <svg class="website__icon" viewBox="0 0 24 24" aria-hidden="true">
      <circle cx="12" cy="12" r="12" fill="#4d4d4f"/>
      <g fill="none" stroke="#fff" stroke-width="1">
        <circle cx="12" cy="12" r="6.5"/>
        <ellipse cx="12" cy="12" rx="3" ry="6.5"/>
        <path d="M5.5 12h13M6.5 9h11M6.5 15h11M12 5.5v13"/>
      </g>
    </svg>
    <span class="website__text">www.lumidrasc.example</span>
  </div>
</section>

</body>
</html>
```